R. T. HOLLOWAY, INC. is a US based Investment firm looking for a five-page website design.

Currently, their temporary site is located at: rtholloway.com and they would like to maintain the site design as much as possible.

R. T. HOLLOWAY, INC. sister companies are: Crestvale Lodge Investments (c-lodge.com) Benwick Petroleum (benwick-petroleum.com) and RTHF (rth-foundation.org/en)

Attached is a .ZIP file with designs and assets we think will be useful for your proposal… Content for the site is attached on: rtholloway website content.docx Current temp website design is attached as: Coming Soon Website.zip .EPS Logo files attached as: rtholloway logos.zip Sample business card attached as: R T Holloway Business cards.eps Other assets, such as Fonts and background images attached as: Assets.zip

Target Market(s)

Investors

Industry/Entity Type

Investments

Number of Pages Required

5+ page

Requirements
Must have
• Contact Page with a form.

```html
<!DOCTYPE html>
<html lang="en">
<head>
<meta charset="utf-8">
<title>R. T. Holloway, Inc.</title>
<link href="https://fonts.googleapis.com/css2?family=Cinzel:wght@400;600;700&family=Mulish:wght@400;500&display=swap" rel="stylesheet">
<style>
  :root {
    --gold: #b49b57;
    --gold-soft: #c9b06a;
    --ink: #222222;
    --text: #3a3a3a;
    --white: #ffffff;
    --night: #000000;
    --hero-dark: #1f1605;
    --hero-mid: #5a4210;
    --line: #2a2a2a;
  }
  * { margin: 0; padding: 0; box-sizing: border-box; }
  html, body { width: 935px; height: 1200px; overflow: hidden; background: var(--white); }
  .page { position: relative; width: 935px; height: 1200px; overflow: hidden; font-family: "Mulish", sans-serif; }

  /* Hero */
  .hero { position: absolute; left: 0; top: 0; width: 935px; height: 467px; }
  .hero-art {
    position: absolute; inset: 0;
    background:
      radial-gradient(ellipse 260px 220px at 660px 210px, rgba(190,150,60,.55), transparent 70%),
      radial-gradient(ellipse 330px 120px at 700px 390px, rgba(170,130,40,.45), transparent 70%),
      linear-gradient(180deg, var(--hero-dark) 0%, var(--hero-mid) 60%, #3e2d09 100%);
  }
  .brand { position: absolute; display: flex; flex-direction: column; align-items: center; color: var(--white); font-family: "Cinzel", serif; font-weight: 600; }
  .brand-mark { border: 2px solid var(--gold); border-radius: 50%; }
  .brand-name { line-height: 1; white-space: nowrap; }
  .brand-sub { line-height: 1; margin-top: 4px; }
  .hero .brand { left: 88px; top: 11px; }
  .hero .brand-mark { width: 34px; height: 34px; margin-bottom: 7px; }
  .hero .brand-name { font-size: 17px; }
  .hero .brand-sub { font-size: 9px; }

  .nav { position: absolute; top: 52px; left: 329px; display: flex; gap: 17px; }
  .nav a { color: var(--white); text-decoration: none; font-family: "Cinzel", serif; font-weight: 600; font-size: 11px; letter-spacing: .4px; }
  .btn-outline {
    position: absolute; display: flex; align-items: center; justify-content: center; gap: 5px;
    border: 1.5px solid var(--gold); border-radius: 20px; color: var(--white);
    font-family: "Cinzel", serif; font-weight: 600; text-decoration: none; letter-spacing: .4px;
  }
  .nav-cta { left: 728px; top: 42px; width: 118px; height: 35px; font-size: 11px; }
  .hero-title { position: absolute; left: 89px; top: 154px; color: var(--white); font-family: "Cinzel", serif; font-weight: 700; font-size: 31px; line-height: 38px; }
  .hero-lead { position: absolute; left: 89px; top: 233px; width: 420px; color: var(--white); font-size: 20px; line-height: 25.5px; }
  .hero-cta { left: 89px; top: 326px; width: 164px; height: 35px; font-size: 11px; }

  /* Investment areas */
  .areas-title { position: absolute; top: 528px; left: 0; width: 935px; text-align: center; font-family: "Cinzel", serif; font-weight: 600; font-size: 26px; color: var(--ink); letter-spacing: .5px; }
  .areas-intro { position: absolute; top: 567px; left: 160px; width: 615px; text-align: center; font-size: 12.4px; line-height: 20.5px; color: var(--text); }
  .areas-chart { position: absolute; left: 0; top: 620px; }
  .area-label { font-family: "Cinzel", serif; font-weight: 600; font-size: 14px; fill: var(--ink); letter-spacing: .4px; }
  .center-name { font-family: "Cinzel", serif; font-weight: 600; font-size: 10px; fill: var(--gold); }

  /* Footer */
  .footer { position: absolute; left: 0; top: 999px; width: 935px; height: 201px; background: var(--night); color: var(--white); }
  .footer .brand { left: 88px; top: 36px; }
  .footer .brand-mark { width: 38px; height: 38px; margin-bottom: 7px; }
  .footer .brand-name { font-size: 19px; }
  .footer .brand-sub { font-size: 10px; }
  .contact-item { position: absolute; top: 51px; display: flex; gap: 13px; }
  .contact-icon { width: 37px; height: 37px; border: 1.5px solid var(--gold); border-radius: 50%; display: flex; align-items: center; justify-content: center; flex: none; }
  .contact-label { font-family: "Cinzel", serif; font-weight: 600; font-size: 12px; letter-spacing: .5px; margin-top: 2px; }
  .contact-value { font-size: 11.5px; line-height: 14px; margin-top: 6px; }
  .contact-value.small { font-size: 10px; line-height: 14px; margin-top: 4px; }
  .divider { position: absolute; left: 88px; top: 150px; width: 759px; height: 1px; background: #2b2b2b; }
  .copyright { position: absolute; left: 89px; top: 167px; font-size: 10px; }
  .social { position: absolute; left: 741px; top: 162px; display: flex; gap: 6px; }
  .social span { width: 22px; height: 22px; border: 1px solid var(--white); border-radius: 50%; }
</style>
</head>
<body>
<div class="page">

  <header class="hero">
    <div class="hero-art" role="img" aria-label="Golden network globe held above an open hand on a dark background"></div>
    <div class="brand">
      <span class="brand-mark"></span>
      <span class="brand-name">R. T. HOLLOWAY</span>
      <span class="brand-sub">INC.</span>
    </div>
    <nav class="nav">
      <a href="#">Home</a>
      <a href="#">About Us</a>
      <a href="#">Investment Areas</a>
      <a href="#">Social Responsibility</a>
    </nav>
    <a class="btn-outline nav-cta" href="#">Contact Us
      <svg width="11" height="6" viewBox="0 0 11 6"><path d="M0 3h9M7 .5 10 3 7 5.5" stroke="#fff" stroke-width="1.4" fill="none"/></svg></a>
    <h1 class="hero-title">Welcome To<br>R. T. Holloway, Inc</h1>
    <p class="hero-lead">R. T. Holloway, Inc. Helps Develop Into A Great Nation And, With Assertiveness, Stamp Its Footprint Worldwide</p>
    <a class="btn-outline hero-cta" href="#">Contact Us Today
      <svg width="11" height="6" viewBox="0 0 11 6"><path d="M0 3h9M7 .5 10 3 7 5.5" stroke="#fff" stroke-width="1.4" fill="none"/></svg></a>
  </header>

  <section class="areas">
    <h2 class="areas-title">Our Investment Areas</h2>
    <p class="areas-intro">Lorem ipsum dolor sit amet, consectetuer adipiscing elit, sed diam nonummy nibh euismod tincidunt ut laoreet dolore magna aliquam erat volutpat. Ut wisi enim ad minim veniam, quis.</p>

    <svg class="areas-chart" width="935" height="330" viewBox="0 620 935 330">
      <defs>
        <filter id="softShadow" x="-30%" y="-30%" width="160%" height="160%">
          <feDropShadow dx="0" dy="1" stdDeviation="4" flood-color="#000" flood-opacity=".12"/>
        </filter>
      </defs>
      <!-- connectors -->
      <g stroke="#555" stroke-width=".7">
        <line x1="277" y1="781" x2="394" y2="781"/>
        <line x1="540" y1="781" x2="657" y2="781"/>
        <line x1="395" y1="727" x2="410" y2="737"/>
        <line x1="539" y1="727" x2="524" y2="737"/>
        <line x1="395" y1="836" x2="410" y2="826"/>
        <line x1="539" y1="836" x2="524" y2="826"/>
      </g>
      <!-- hub -->
      <circle cx="467" cy="781" r="73" fill="none" stroke="#555" stroke-width=".8" stroke-dasharray="1.5 2"/>
      <circle cx="467" cy="781" r="60" fill="#fff" filter="url(#softShadow)"/>
      <circle cx="467" cy="781" r="40" fill="none" stroke="var(--gold)" stroke-width="3.5"/>
      <text class="center-name" x="467" y="785" text-anchor="middle">R. T. HOLLOWAY</text>

      <!-- left-side areas: gold arc on the left -->
      <g fill="none">
        <circle cx="335" cy="700" r="65" stroke="var(--line)" stroke-width=".8"/>
        <path d="M338 632 A68 68 0 0 0 338 768" stroke="var(--gold)" stroke-width="6"/>
        <circle cx="209" cy="781" r="65" stroke="var(--line)" stroke-width=".8"/>
        <path d="M212 713 A68 68 0 0 0 212 849" stroke="var(--gold)" stroke-width="6"/>
        <circle cx="335" cy="864" r="65" stroke="var(--line)" stroke-width=".8"/>
        <path d="M338 796 A68 68 0 0 0 338 932" stroke="var(--gold)" stroke-width="6"/>
      </g>
      <!-- right-side areas: gold arc on the right -->
      <g fill="none">
        <circle cx="600" cy="700" r="65" stroke="var(--line)" stroke-width=".8"/>
        <path d="M597 632 A68 68 0 0 1 597 768" stroke="var(--gold)" stroke-width="6"/>
        <circle cx="725" cy="781" r="65" stroke="var(--line)" stroke-width=".8"/>
        <path d="M722 713 A68 68 0 0 1 722 849" stroke="var(--gold)" stroke-width="6"/>
        <circle cx="600" cy="864" r="65" stroke="var(--line)" stroke-width=".8"/>
        <path d="M597 796 A68 68 0 0 1 597 932" stroke="var(--gold)" stroke-width="6"/>
      </g>
      <!-- joints -->
      <g fill="var(--gold)">
        <circle cx="395" cy="727" r="5.5"/>
        <circle cx="539" cy="727" r="5.5"/>
        <circle cx="277" cy="781" r="5.5"/>
        <circle cx="657" cy="781" r="5.5"/>
        <circle cx="395" cy="836" r="5.5"/>
        <circle cx="539" cy="836" r="5.5"/>
      </g>
      <!-- area icons -->
      <g fill="#efe6cc">
        <rect x="297" y="664" width="36" height="38" rx="4" role="img" aria-label="Real estate icon: house above a handshake"/>
        <rect x="171" y="748" width="42" height="36" rx="4" role="img" aria-label="Healthcare icon: heart above an open hand"/>
        <rect x="329" y="833" width="42" height="36" rx="4" role="img" aria-label="Finance icon: coin with a stack of coins"/>
        <rect x="558" y="664" width="44" height="38" rx="4" role="img" aria-label="Energy icon: lightning bolt in circling arrows"/>
        <rect x="682" y="745" width="38" height="38" rx="4" role="img" aria-label="Mining icon: coins with a pickaxe"/>
        <rect x="558" y="830" width="36" height="36" rx="4" role="img" aria-label="Industry icon: factory building"/>
      </g>
      <!-- labels -->
      <text class="area-label" x="296" y="725">Real Estate</text>
      <text class="area-label" x="170" y="807">Healthcare</text>
      <text class="area-label" x="296" y="890">Finance</text>
      <text class="area-label" x="558" y="725">Energy</text>
      <text class="area-label" x="681" y="807">Mining</text>
      <text class="area-label" x="558" y="890">Industry</text>
    </svg>
  </section>

  <footer class="footer">
    <div class="brand">
      <span class="brand-mark"></span>
      <span class="brand-name">R. T. HOLLOWAY</span>
      <span class="brand-sub">INC.</span>
    </div>

    <div class="contact-item" style="left:285px">
      <span class="contact-icon"><svg width="16" height="16" viewBox="0 0 24 24"><path d="M5 3h4l2 5-2.5 1.5a11 11 0 0 0 6 6L16 13l5 2v4a2 2 0 0 1-2 2A16 16 0 0 1 3 5a2 2 0 0 1 2-2z" fill="none" stroke="var(--gold)" stroke-width="1.5"/></svg></span>
      <div><div class="contact-label">Phone</div><div class="contact-value">123-456-7890</div></div>
    </div>
    <div class="contact-item" style="left:441px">
      <span class="contact-icon"><svg width="14" height="18" viewBox="0 0 14 18"><path d="M7 17s6-6.5 6-10.5A6 6 0 0 0 1 6.5C1 10.5 7 17 7 17z" fill="none" stroke="var(--gold)" stroke-width="1.3"/><circle cx="7" cy="6.5" r="2.2" fill="none" stroke="var(--gold)" stroke-width="1.3"/></svg></span>
      <div><div class="contact-label">Address</div><div class="contact-value small">123 Lorem ipsum dolor sit amet,<br>consectetuer adipiscing.</div></div>
    </div>
    <div class="contact-item" style="left:674px">
      <span class="contact-icon"><svg width="17" height="15" viewBox="0 0 17 15"><path d="M1 6v8h15V6L8.5 1z M1 6l7.5 5L16 6" fill="none" stroke="var(--gold)" stroke-width="1.2"/></svg></span>
      <div><div class="contact-label">Email</div><div class="contact-value">info@rthollowayinc.com</div></div>
    </div>

    <div class="divider"></div>
    <p class="copyright">Copyright © 2021 R.T Holloway Inc.. All Rights Reserved.</p>
    <div class="social" aria-label="Social media links"><span></span><span></span><span></span><span></span></div>
  </footer>

</div>
</body>
</html>
```